Urgent Care Postcard Launch

We are launching a pediatric only urgent care. The postcard will be hand-delivered to local medical providers and business owners.
Updates

Reason: I was traveling with spotty internet and was unable to provide feedback. Thanks for your understanding!

All designs need to have a focus on Urgent Care. Where the lines say "opening soon" it needs to be specific to Urgent Care as a we are already open for primary care. Thanks.

Target Market(s)

Parents/grandparents of children 0-17 years old.

Industry/Entity Type

Medical

Requirements
Must have
• Opening date of September 1, 2014
Hours of operation - weekdays 5pm-9pm/weekends and holidays 9am-5pm
Phone #(405)555-0193
website - www.larchfieldmd.com
Logo
List of things we can treat (see previous flyers)

```html
<!DOCTYPE html>
<html lang="en">
<head>
<meta charset="utf-8">
<title>Larchfield Pediatrics – Urgent Care Postcard</title>
<link rel="stylesheet" href="https://fonts.googleapis.com/css2?family=Open+Sans:wght@400;600;700;800&family=Montserrat:wght@600;700&display=swap">
<style>
  :root {
    --stage: #5d5d5f;
    --paper: #ffffff;
    --green: #4bb04a;
    --green-dark: #2e9a3a;
    --red: #d7262f;
    --ink: #1d1d1d;
    --grey-text: #333333;
    --map-yellow: #f2e600;
    --photo-grass-top: #9cc76a;
    --photo-grass-bottom: #5f9d34;
  }
  * { box-sizing: border-box; margin: 0; padding: 0; }
  html, body { width: 776px; height: 1200px; overflow: hidden; }
  body { background: var(--stage); font-family: "Open Sans", Arial, sans-serif; position: relative; color: var(--ink); }

  .card { position: absolute; left: 48px; width: 679px; height: 520px; background: var(--paper); overflow: hidden; }
  .card--front { top: 50px; }
  .card--back { top: 615px; }

  /* Front */
  .hero-photo { position: absolute; left: 0; top: 0; width: 679px; height: 390px;
    background: linear-gradient(180deg, var(--photo-grass-top) 0%, #7fb551 45%, var(--photo-grass-bottom) 100%); }
  .hero-title { position: absolute; top: 22px; left: 0; width: 100%; text-align: center;
    color: #fff; font-weight: 800; font-size: 43px; letter-spacing: 0.5px; text-shadow: 0 2px 4px rgba(0,0,0,.35); }
  .opening-badge { position: absolute; left: 28px; top: 180px; width: 178px; height: 178px; border-radius: 50%;
    background: var(--green); border: 6px solid #fff; box-shadow: 0 2px 6px rgba(0,0,0,.3);
    display: flex; flex-direction: column; align-items: center; justify-content: center; }
  .opening-badge__inner { transform: rotate(-20deg); text-align: center; line-height: 1; }
  .opening-badge__lead { color: #ffe600; font-weight: 800; font-size: 30px; display: block; }
  .opening-badge__date { color: #fff; font-weight: 700; font-size: 16px; display: block; margin-top: 6px; line-height: 1.15; }

  .front-info { position: absolute; left: 0; top: 390px; width: 100%; height: 130px; }
  .call-now { position: absolute; left: 56px; top: 14px; color: var(--red); font-size: 22px; }
  .website { position: absolute; left: 77px; top: 44px; color: var(--green-dark); font-weight: 700; font-size: 19px; }
  .hours-title { position: absolute; left: 117px; top: 75px; font-size: 16px; color: var(--ink); }
  .hours { position: absolute; left: 22px; top: 98px; font-size: 14px; color: var(--ink); }

  .brand { position: absolute; display: flex; align-items: center; gap: 8px; }
  .brand__mark { width: 16px; height: 16px; background: var(--red); }
  .brand__name { font-family: "Montserrat", Arial, sans-serif; font-weight: 700; color: var(--red); line-height: 1.05; }
  .brand--front { left: 445px; top: 430px; }
  .brand--front .brand__name { font-size: 21px; }
  .brand--footer { left: 30px; top: 455px; }
  .brand--footer .brand__name { font-size: 13px; }

  /* Back */
  .photo-frame { position: absolute; left: 22px; width: 168px; height: 134px; border: 4px solid var(--red); border-radius: 16px; }
  .photo-frame--baby { top: 25px; background: linear-gradient(135deg, #f4ece6, #d9c4b4); }
  .photo-frame--vaccine { top: 190px; background: linear-gradient(135deg, #f2f2f4, #e5a9c3); }

  .intro { position: absolute; left: 214px; top: 24px; width: 440px; font-size: 14px; line-height: 1.5; color: var(--grey-text); }
  .intro strong { color: var(--ink); font-weight: 700; }

  .services { position: absolute; top: 114px; list-style: none; font-family: "Montserrat", Arial, sans-serif; font-weight: 600; font-size: 14px; color: var(--ink); }
  .services li { height: 20.6px; line-height: 20.6px; white-space: nowrap; }
  .services li::before { content: "•"; color: var(--red); margin-right: 4px; }
  .services--left { left: 210px; }
  .services--right { left: 446px; }

  .tagline-band { position: absolute; left: 0; top: 370px; width: 100%; height: 63px; background: var(--green); }
  .tagline { position: absolute; left: 30px; top: 9px; width: 380px; text-align: center; color: #fff; font-weight: 700; font-size: 16.5px; line-height: 1.3; }

  .map { position: absolute; left: 426px; top: 351px; width: 233px; height: 156px; border: 4px solid var(--map-yellow); border-radius: 14px;
    background: linear-gradient(160deg, #ecebe6, #dcdad2); }

  .divider { position: absolute; left: 184px; top: 451px; width: 1px; height: 57px; background: #666; }
  .address { position: absolute; left: 202px; top: 460px; font-size: 15px; line-height: 1.35; color: var(--grey-text); letter-spacing: 0.2px; }
</style>
</head>
<body>

<section class="card card--front">
  <div class="hero-photo" role="img" aria-label="Photo of a laughing mother and young son lying together on green grass"></div>
  <h1 class="hero-title">PEDIATRIC URGENT CARE</h1>
  <div class="opening-badge">
    <div class="opening-badge__inner">
      <span class="opening-badge__lead">OPENING<br>SOON</span>
      <span class="opening-badge__date">SEPTEMBER<br>1, 2014</span>
    </div>
  </div>
  <div class="front-info">
    <p class="call-now">CALL NOW : (405)555-0193</p>
    <p class="website">WWW.LARCHFIELDMD.COM</p>
    <p class="hours-title">HOURS OF OPERATION</p>
    <p class="hours">weekdays 5pm-9pm/weekends and holidays 9am-5pm</p>
  </div>
  <div class="brand brand--front">
    <span class="brand__mark"></span>
    <span class="brand__name">LARCHFIELD<br>PEDIATRICS</span>
  </div>
</section>

<section class="card card--back">
  <div class="photo-frame photo-frame--baby" role="img" aria-label="Photo of a smiling baby being examined with a stethoscope"></div>
  <div class="photo-frame photo-frame--vaccine" role="img" aria-label="Photo of a young girl receiving an immunization shot"></div>

  <p class="intro">When your child gets sick the illness often seems to escalate quickly. That’s why at Larchfield Pediatrics we offer <strong>full service pediatric care!</strong> We are dedicated to giving your children high quality care when they need it the most.</p>

  <ul class="services services--left">
    <li>Allergies</li>
    <li>Colds and Flu</li>
    <li>Fever</li>
    <li>Flu Shots and Immunizations</li>
    <li>Ear Infections</li>
    <li>Fractures</li>
    <li>Lacerations or Cut Repair</li>
    <li>Stomach Aches</li>
    <li>Sprains and Strains</li>
    <li>Sore Throats</li>
    <li>Vomiting and Diarrhea</li>
  </ul>
  <ul class="services services--right" style="top:110px">
    <li>Asthma Attacks (Minor)</li>
    <li>Eye Injury (Minor)</li>
    <li>Migraine</li>
    <li>Injuries</li>
    <li>Wellness Exams</li>
    <li>Pregnancy Testing</li>
    <li>Physicals</li>
    <li>Skin Rashes</li>
    <li>Urinary and Gynecological</li>
    <li>Infections</li>
    <li>Wart and Skin Tag Removal</li>
  </ul>

  <div class="tagline-band">
    <p class="tagline">BECAUSE NOTHING MATTERS MORE<br>THAN YOUR CHILD’S HEALTH.</p>
  </div>
  <div class="map" role="img" aria-label="Street map showing the clinic location in southwest Oklahoma City"></div>

  <div class="brand brand--footer">
    <span class="brand__mark"></span>
    <span class="brand__name">LARCHFIELD<br>PEDIATRICS</span>
  </div>
  <div class="divider"></div>
  <p class="address">4410 SW 96TH<br>OKLAHOMA CITY, OK 73159</p>
</section>

</body>
</html>
```